Kelmo bottle Label (Yoghurt drink)

Label for a 300 ml yoghurt drink bottle in 3 flavours.

General description:
• This is to design a sleeve shrink label for a Yoghurt Drink bottle in three flavours, Classic, Strawberry and Blueberry.
• Attached 3 photos: The one with KELMO brand in the current design we want to replace using the same bottle.
• Graphically, the design is to be similar to the examples provided for trevanu and fizzlotop.
• Use font and barcode size to be readable and legal.
• Minimize the use of the upper third of the bottle as it will be distorted when the label shrinks to the bottle.
• Professional and experienced designers only are welcome, please do not waste your time otherwise.

Bottle dimensions:
• Base across: 61 mm
• Height: 145 mm (approximate)

Graphical description:
• White colour with bands at the top and bottom similar to the one in “trevanu” example provided (not necessarily identical, feel free to be creative.
• The upper and lower bands to be: Green for “classic”, Pink or red for strawberry and purple for blueberry flavour.
• On the front: the brand name “Kelmo” and description “Yoghurt Drink” to be graphically attractive.
• On the front: two or more pieces of strawberry or blueberry for each flavour placed nicely with the option to include “yoghurt splash” or any suitable affects you deem suitable.
• For the Classic flavour, use the words (Classic, Lassi, Ayran) in the same location for the berries done in a graphically suitable manner.
• Colour temperature for the three flavours to be similar.

Information and objects on the label:
Front:
• The word “Kelmo” (brand name)
• “Yoghurt drink” (Product description)
• “300 ml” (size)
• Picture of Strawberries for strawberry flavour.
• Picture of Blueberries for blueberry flavour.
• The words (Classic, Lassi, Ayran) in the place used for the strawberries in the flavoured type, distributed to look graphically suitable for the overall design.

Back:
• Ingredient: Milk/milk solids, culture, salt, water, sugar, colour, flavour. (this is to be finalized later)
• Nutrition information table: (to be provided later).
• Barcode (to be provided later)
• Product of Australia
• Feluna Ristov Pty Ltd, 7/4 Corran Rd, Malaga, WA 6090
• info@kelmo-example.com.au 0491862037
• Keep under 5⁰ C
• Best before date printed on the bottle
• Shake well (to be located on the side at the top)
• Recycle icon.

Health benefits: (to be located suitably, possibly on the side with vertical orientation)
• Rich in probiotic bacteria and vitamins.
• Improves digestion and bowel motion.
• Supports weight control and fat loss.

Target Market(s)

General consumers

Industry/Entity Type

Grocery Store

Font styles to use
Sans Serif

Colors
abd037
b768aa
f04a50

Requirements
Must have
• The details in the project description
• The design must be simple and neat.
• Please use the shape of the current bottle "Kelmo" as in the attached photo.
Should not have
• Busy, cluttered, or empty and incomplete designs.

```html
<!DOCTYPE html>
<html lang="en">
<head>
<meta charset="utf-8">
<title>Kelmo Yoghurt Drink – Strawberry Label</title>
<link rel="stylesheet" href="https://fonts.googleapis.com/css2?family=Fira+Sans+Extra+Condensed:wght@400;700&family=Roboto:wght@300;700&display=swap">
<style>
  :root {
    --band-dark: #b8282e;
    --band-light: #e2787c;
    --band-stripe: #e88a8f;
    --rule-grey: #d9d9d9;
    --brand-pink: #d75b66;
    --descriptor-grey: #8e8f91;
    --flavour-red: #c0272d;
    --label-white: #ffffff;
    --ring-red: #d4555c;
    --capsule-grey: #ececec;
  }
  html, body {
    margin: 0;
    padding: 0;
    overflow: hidden;
    background: var(--label-white);
  }
  .label {
    position: relative;
    width: 1200px;
    height: 2848px;
    background: var(--label-white);
    overflow: hidden;
    font-family: "Fira Sans Extra Condensed", sans-serif;
  }
  .band-top {
    position: absolute;
    left: 0; top: 0;
    width: 1200px; height: 99px;
    background: linear-gradient(to bottom, var(--band-dark), var(--band-light));
  }
  .rule-top {
    position: absolute;
    left: 0; top: 103px;
    width: 1200px; height: 15px;
    background: var(--rule-grey);
  }
  .emblem {
    position: absolute;
    left: 0; top: 0;
  }
  .brand-name {
    position: absolute;
    left: 0; top: 1685px;
    width: 1200px;
    margin: 0;
    text-align: center;
    font-weight: 700;
    font-size: 400px;
    line-height: 1;
    letter-spacing: 0;
    white-space: nowrap;
    color: var(--brand-pink);
  }
  .descriptor {
    position: absolute;
    left: 0; top: 2112px;
    width: 1200px;
    margin: 0;
    text-align: center;
    font-family: "Roboto", sans-serif;
    font-weight: 300;
    font-size: 92px;
    line-height: 1;
    letter-spacing: 8px;
    white-space: nowrap;
    color: var(--descriptor-grey);
  }
  .descriptor strong { font-weight: 700; }
  .flavour {
    position: absolute;
    left: 0; top: 2255px;
    width: 1200px;
    margin: 0;
    text-align: center;
    font-weight: 400;
    font-size: 122px;
    line-height: 1;
    color: var(--flavour-red);
  }
  .stripe-bottom {
    position: absolute;
    left: 0; top: 2567px;
    width: 1200px; height: 21px;
    background: var(--band-stripe);
  }
  .band-bottom {
    position: absolute;
    left: 0; top: 2611px;
    width: 1200px; height: 237px;
    background: linear-gradient(to bottom, var(--band-light), var(--band-dark));
    color: var(--label-white);
    font-size: 64px;
    line-height: 1;
  }
  .band-bottom .claim {
    position: absolute;
    left: 42px; top: 112px;
  }
  .band-bottom .volume {
    position: absolute;
    right: 58px; top: 112px;
  }
</style>
</head>
<body>
<div class="label">
  <div class="band-top"></div>
  <div class="rule-top"></div>

  <svg class="emblem" width="1200" height="1500" viewBox="0 0 1200 1500">
    <defs>
      <filter id="capsule-shadow" x="-20%" y="-20%" width="140%" height="140%">
        <feDropShadow dx="10" dy="22" stdDeviation="18" flood-color="#000" flood-opacity="0.22"/>
      </filter>
      <radialGradient id="fruit-fill" cx="0.45" cy="0.45" r="0.6">
        <stop offset="0" stop-color="#e4353a"/>
        <stop offset="1" stop-color="#a8161c"/>
      </radialGradient>
    </defs>
    <g class="capsule" filter="url(#capsule-shadow)" fill="var(--capsule-grey)">
      <circle cx="336" cy="478" r="250"/>
      <circle cx="760" cy="1082" r="338"/>
      <line x1="336" y1="478" x2="760" y2="1082" stroke="var(--capsule-grey)" stroke-width="300" stroke-linecap="round"/>
    </g>
    <circle cx="336" cy="478" r="200" fill="#fafafa"/>
    <circle cx="760" cy="1082" r="272" fill="#fafafa"/>

    <circle class="ring" cx="336" cy="478" r="161" fill="#ffffff" stroke="var(--ring-red)" stroke-width="6"/>
    <circle cx="336" cy="478" r="120" fill="#eef0f2" role="img" aria-label="Brand emblem area"/>

    <circle class="ring" cx="760" cy="1082" r="218" fill="#ffffff" stroke="var(--ring-red)" stroke-width="6"/>
    <ellipse cx="750" cy="1092" rx="170" ry="110" fill="url(#fruit-fill)" role="img" aria-label="Two ripe strawberries with green leaves"/>
  </svg>

  <h1 class="brand-name">KELMO</h1>
  <p class="descriptor">YOGHURT <strong>DRINK</strong></p>
  <p class="flavour">Strawberry</p>

  <div class="stripe-bottom"></div>
  <div class="band-bottom">
    <span class="claim">100% Natural Ingredients</span>
    <span class="volume">300ml.</span>
  </div>
</div>
</body>
</html>
```